Marlow & Tate
Business card and stationery design for a management consulting firm  - Consulting
Simple
Benedikt Owen Dolsquin
Lead Consultant
Njegoševa 47 11000 Belgrade
benedikt.owen@marlowtate-example.com
www.marlowtate-example.com
Keep the design clean. "Scandinavian design approach". Address line on business card is preferred not to be included, although if designer finds it to complete the holistic 'picture' of the card, then he/she may use it. Font selection for the rest of the text is up to the designer. Although please note that the font has to be in balance with the logo. Business cards are to be printed on black paper / metal. If printed on paper, the logo part will be with relief printing.
This is designers choice to be creative
dolsquin dolsquin
Tip to designers: Try not to use the monogram "MT" with "Marlow and Tate" on the same side. Printing techniques that will be used are: Embossing / Debossing, Thermography. Keep it clean. Less is more.

```html
<!DOCTYPE html>
<html lang="en">
<head>
<meta charset="utf-8">
<title>Marlow and Tate — Business Card</title>
<link href="https://fonts.googleapis.com/css2?family=EB+Garamond:wght@400&display=swap" rel="stylesheet">
<style>
  :root {
    --backdrop: #d9d9d9;
    --card-black: #0c0c0c;
    --card-grey: #b9b9b9;
    --ink-white: #f2f2f2;
    --ink-soft: #cfcfcf;
  }
  html, body {
    margin: 0;
    padding: 0;
    width: 1200px;
    height: 984px;
    overflow: hidden;
    background: var(--backdrop);
    font-family: "EB Garamond", Georgia, serif;
  }
  .canvas {
    position: relative;
    width: 1200px;
    height: 984px;
  }
  .card {
    position: absolute;
    left: 260px;
    width: 680px;
    height: 440px;
    border-radius: 34px;
    overflow: hidden;
    background: var(--card-black);
    box-shadow: 0 10px 24px rgba(0,0,0,0.18);
  }
  .card--front { top: 34px; }
  .card--back { top: 510px; }
  .card__band {
    position: absolute;
    left: 0;
    bottom: 0;
    width: 680px;
    height: 110px;
  }
  .card__band path { fill: var(--card-grey); }

  .brand-name {
    color: var(--ink-white);
    font-weight: 400;
    letter-spacing: 0.02em;
    white-space: nowrap;
  }
  .card--front .brand-name {
    position: absolute;
    top: 178px;
    left: 0;
    width: 100%;
    text-align: center;
    font-size: 46px;
  }
  .card--back .brand-name {
    position: absolute;
    top: 70px;
    left: 54px;
    font-size: 36px;
  }

  .contact {
    position: absolute;
    left: 54px;
    top: 178px;
    margin: 0;
    padding: 0;
    list-style: none;
    color: var(--ink-soft);
    font-size: 17px;
    line-height: 24px;
  }
  .contact__item {
    display: flex;
    align-items: flex-start;
  }
  .contact__icon {
    width: 14px;
    height: 14px;
    margin: 5px 12px 0 0;
    flex: none;
    fill: var(--ink-soft);
  }
  .contact__icon--blank { visibility: hidden; }

  .person {
    position: absolute;
    right: 60px;
    top: 212px;
    text-align: right;
    color: var(--ink-white);
  }
  .person__name {
    margin: 0;
    font-size: 24px;
    font-weight: 400;
  }
  .person__role {
    margin: 4px 0 0;
    font-size: 18px;
    color: var(--ink-soft);
  }
</style>
</head>
<body>
<main class="canvas">

  <section class="card card--front" aria-label="Card front">
    <div class="brand-name">Marlow and Tate</div>
    <svg class="card__band" viewBox="0 0 680 110" aria-hidden="true">
      <path d="M0 30 L200 30 Q214 30 222 42 L250 80 Q258 92 272 92 L680 92 L680 110 L0 110 Z"/>
    </svg>
  </section>

  <section class="card card--back" aria-label="Card back">
    <div class="brand-name">Marlow and Tate</div>

    <ul class="contact">
      <li class="contact__item">
        <svg class="contact__icon" viewBox="0 0 14 14" aria-hidden="true"><path d="M7 0a5 5 0 0 0-5 5c0 3.6 5 9 5 9s5-5.4 5-9a5 5 0 0 0-5-5zm0 7a2 2 0 1 1 0-4 2 2 0 0 1 0 4z"/></svg>
        <span>Njegoševa 47</span>
      </li>
      <li class="contact__item">
        <svg class="contact__icon contact__icon--blank" viewBox="0 0 14 14" aria-hidden="true"></svg>
        <span>11000 Belgrade</span>
      </li>
      <li class="contact__item">
        <svg class="contact__icon" viewBox="0 0 14 14" aria-hidden="true"><path d="M3 0.5 5.2 3.2 4 5a8 8 0 0 0 5 5l1.8-1.2 2.7 2.2-1.4 2.3C6 13 1 8 0.7 1.9z"/></svg>
        <span>381 60 555 0142</span>
      </li>
      <li class="contact__item">
        <svg class="contact__icon" viewBox="0 0 14 14" aria-hidden="true"><path d="M0 3h14v8H0zM1.2 4 7 8l5.8-4v-.1H1.2z" fill-rule="evenodd"/></svg>
        <span>benedikt.owen@marlowtate-example.com</span>
      </li>
      <li class="contact__item">
        <svg class="contact__icon" viewBox="0 0 14 14" aria-hidden="true"><circle cx="7" cy="7" r="6"/></svg>
        <span>www.marlowtate-example.com</span>
      </li>
    </ul>

    <div class="person">
      <p class="person__name">Benedikt Owen Dolsquin</p>
      <p class="person__role">Lead Consultant</p>
    </div>

    <svg class="card__band" viewBox="0 0 680 110" aria-hidden="true">
      <path d="M0 42 L330 42 Q346 42 356 54 L384 86 Q394 96 410 96 L680 96 L680 110 L0 110 Z"/>
    </svg>
  </section>

</main>
</body>
</html>
```